Business Card Design

we are a small based family business that specialise in 12v led lights for kelvo caravans.
we also sell 12v switches, wire, circuit breakers, dimmers etc but our main line is LEDs.
We would like something that reflects the LED lighting on our cards.
www.willowtreeleds.com.au is where you can have a look at to get ideas, of our product.
I have attached the logo we generally use on all our tradio listings and is the main header on our website.

Look forward to seeing what your team comes up with.

Industry/Entity Type

Business

Contact Information for Business Card

Tam 0491 738 205
Cedarwood Vale QLD 4312

www.willowtreeleds.com

```html
<!DOCTYPE html>
<html lang="en">
<head>
<meta charset="utf-8">
<title>Willow Tree LEDs – Business Card</title>
<link rel="stylesheet" href="https://fonts.googleapis.com/css2?family=Open+Sans:wght@600;700;800&display=swap">
<style>
  :root {
    --backdrop: #8a4a28;
    --sky-top: #2fa6dc;
    --sky-mid: #8fd0ee;
    --sky-low: #f4fbff;
    --brand-red: #b12a26;
    --ink: #1d1d1d;
    --white: #ffffff;
    --caption: rgba(70, 165, 220, 0.88);
    --swoosh: #111111;
  }
  * { margin: 0; padding: 0; box-sizing: border-box; }
  html, body {
    width: 1200px; height: 800px; overflow: hidden;
    background: var(--backdrop);
    font-family: "Open Sans", Arial, sans-serif;
  }
  .canvas { position: relative; width: 1200px; height: 800px; }

  .card {
    position: absolute;
    border-radius: 18px;
    overflow: hidden;
    box-shadow: 0 6px 14px rgba(0,0,0,0.35);
  }

  /* Front */
  .card-front {
    left: 228px; top: 82px; width: 559px; height: 328px;
    background: linear-gradient(180deg, var(--sky-top) 0%, var(--sky-mid) 55%, var(--sky-low) 100%);
  }
  .brand-name {
    font-weight: 800;
    color: var(--brand-red);
    letter-spacing: -0.3px;
    white-space: nowrap;
  }
  .card-front .brand-name {
    position: absolute; left: 0; right: 0; top: 62px;
    text-align: center; font-size: 22px;
  }
  .product-tile {
    position: absolute; top: 130px; width: 143px; height: 93px;
    overflow: hidden;
  }
  .product-tile:nth-of-type(1) { left: 51px; }
  .product-tile:nth-of-type(2) { left: 205px; }
  .product-tile:nth-of-type(3) { left: 360px; }
  .product-photo { position: absolute; inset: 0; }
  .photo-interior { background: linear-gradient(135deg, #6b3a1f 0%, #b07a4a 45%, #e6dccb 100%); }
  .photo-dimmer { background: linear-gradient(135deg, #f2f2f2 0%, #d9dedd 50%, #9fb6b0 100%); }
  .photo-awning { background: linear-gradient(135deg, #0f1620 0%, #3a4a5c 55%, #d7e3ee 100%); }
  .product-caption {
    position: absolute; left: 0; right: 0; bottom: 0; height: 16px;
    background: var(--caption);
    color: var(--white);
    font-size: 10.5px; font-weight: 700;
    line-height: 16px; padding-left: 8px;
    text-transform: uppercase;
  }
  .tagline {
    position: absolute; left: 0; right: 0; top: 251px;
    text-align: center;
    font-size: 13px; font-weight: 700; color: var(--ink);
    letter-spacing: 0.3px;
  }

  /* Back */
  .card-back {
    left: 228px; top: 425px; width: 554px; height: 323px;
    background: var(--white);
  }
  .back-shapes { position: absolute; inset: 0; }
  .card-back .brand-name {
    position: absolute; left: 45px; top: 62px; font-size: 22px;
  }
  .holder-name {
    position: absolute; left: 45px; top: 257px;
    color: var(--white); font-size: 16px; font-weight: 700;
  }
  .contact-list {
    position: absolute; right: 32px; top: 238px;
    list-style: none;
  }
  .contact-list li {
    display: flex; align-items: center; justify-content: flex-end;
    gap: 8px; height: 21px;
    color: var(--white); font-size: 13px; font-weight: 600;
  }
  .contact-list svg { width: 13px; height: 13px; flex: none; }
</style>
</head>
<body>
<main class="canvas">

  <section class="card card-front">
    <div class="brand-name">Willow Tree LEDs</div>

    <figure class="product-tile">
      <div class="product-photo photo-interior" role="img" aria-label="Photo of a caravan interior lit by LED lights"></div>
      <figcaption class="product-caption">Interior Lighting</figcaption>
    </figure>
    <figure class="product-tile">
      <div class="product-photo photo-dimmer" role="img" aria-label="Photo of an LED dimmer control panel"></div>
      <figcaption class="product-caption">LED Dimmers</figcaption>
    </figure>
    <figure class="product-tile">
      <div class="product-photo photo-awning" role="img" aria-label="Photo of awning lights glowing at night at a campsite"></div>
      <figcaption class="product-caption">Awning Lights</figcaption>
    </figure>

    <p class="tagline">LED LIGHTING SOLUTIONS FOR CAMPING, CARAVANING AND BOATING</p>
  </section>

  <section class="card card-back">
    <svg class="back-shapes" viewBox="0 0 554 323" preserveAspectRatio="none" aria-hidden="true">
      <path fill="var(--brand-red)" d="M0,220 C150,212 330,200 430,120 C480,80 510,35 535,0 L554,0 L554,323 L0,323 Z"/>
      <path fill="var(--swoosh)" d="M0,168 C150,158 320,172 412,128 C330,182 160,190 0,212 Z"/>
    </svg>

    <div class="brand-name">Willow Tree LEDs</div>
    <p class="holder-name">TAM</p>

    <ul class="contact-list">
      <li>0491 738 205
        <svg viewBox="0 0 16 16"><path fill="var(--white)" d="M3.5 1.5l2.3 0 1.2 3.2-1.6 1.1c.8 1.7 2.1 3 3.8 3.8l1.1-1.6 3.2 1.2v2.3c0 .8-.7 1.5-1.5 1.5C6.5 13 3 9.5 2 3c0-.8.7-1.5 1.5-1.5z"/></svg>
      </li>
      <li>www.willowtreeleds.com.au
        <svg viewBox="0 0 16 16"><circle cx="8" cy="8" r="6.5" fill="none" stroke="var(--white)" stroke-width="1.5"/><ellipse cx="8" cy="8" rx="2.6" ry="6.5" fill="none" stroke="var(--white)" stroke-width="1.2"/><line x1="1.5" y1="8" x2="14.5" y2="8" stroke="var(--white)" stroke-width="1.2"/></svg>
      </li>
      <li>18 Paperbark Street, Cedarwood Vale, QLD 4312
        <svg viewBox="0 0 16 16"><path fill="var(--white)" d="M8 1a5 5 0 0 0-5 5c0 3.6 5 9 5 9s5-5.4 5-9a5 5 0 0 0-5-5zm0 7a2 2 0 1 1 0-4 2 2 0 0 1 0 4z"/></svg>
      </li>
    </ul>
  </section>

</main>
</body>
</html>
```